MapleTrove shopping service flyer

We are a Korean shopping service. The attached picture explains our service. We would like to create a postcard or slightly larger sized flyer advertising our service. Front side will be graphics and back side text. For the front side, we want an updated version of the attached picture with our new logo and colours. And for the back side, create a simple design on the back side which we can enter all the text. Need font and design options.

Target Market(s)

20s and 30s females shopping for clothing (people not in Korea), shoppers are not Korean.

Industry/Entity Type

Online Shopping

Requirements
Must have
• For the front side, we want an updated version of the attached picture with our new logo and colours. And for the back side, create a simple design on the back side which we can enter all the text. Need font and design options.
Nice to have
• Little to no text on the front side.

```html
<!DOCTYPE html>
<html lang="en">
<head>
<meta charset="utf-8">
<title>MapleTrove shopping service flyer</title>
<link rel="stylesheet" href="https://fonts.googleapis.com/css2?family=Montserrat:wght@500;600;700;800&display=swap">
<style>
  :root {
    --bg: #5fb0d6;
    --teal: #17968a;
    --teal-deep: #138476;
    --pink: #e0197a;
    --orange: #f0a93a;
    --white: #ffffff;
    --ink: #2f3a40;
    --screen-blue: #149bb0;
  }
  * { box-sizing: border-box; margin: 0; padding: 0; }
  html, body { width: 1200px; height: 800px; overflow: hidden; }
  body {
    background: var(--bg);
    font-family: "Montserrat", Arial, sans-serif;
    position: relative;
  }
  .card {
    position: absolute;
    top: 213px;
    width: 560px;
    height: 374px;
    overflow: hidden;
    background: var(--teal);
    box-shadow: 0 10px 24px rgba(0, 40, 70, 0.25);
  }
  .card--front { left: 30px; }
  .card--back { left: 610px; }
  .card__art { position: absolute; inset: 0; width: 100%; height: 100%; }
  .card__text { position: absolute; color: var(--white); }

  /* Front */
  .tagline-vertical {
    left: 30px; top: 133px;
    font-size: 15px; font-weight: 500;
    transform: rotate(-90deg); transform-origin: left top;
    white-space: nowrap;
  }
  .headline {
    left: 52px; top: 48px;
    font-size: 48px; font-weight: 800; line-height: 46px; letter-spacing: 1px;
  }
  .headline__divider {
    position: absolute; left: 170px; top: 98px;
    width: 5px; height: 113px; background: var(--white);
  }
  .offer {
    right: 412px; top: 148px;
    text-align: right; font-size: 13px; font-weight: 500; line-height: 16px;
  }
  .brand-badge {
    position: absolute; left: -5px; top: 250px;
    width: 130px; height: 130px; border-radius: 50%;
    background: var(--white);
    display: flex; align-items: center; justify-content: center;
  }
  .brand-badge__name {
    color: var(--teal-deep); font-size: 16px; font-weight: 700;
    margin-left: 12px; margin-bottom: 10px;
  }

  /* Back */
  .back-title {
    left: 0; width: 536px; top: 22px; text-align: center;
    font-size: 26px; font-weight: 800; letter-spacing: -1px;
  }
  .step {
    display: flex; align-items: center; gap: 5px;
    font-size: 11px; font-weight: 700; line-height: 12px;
    white-space: nowrap;
  }
  .step__num {
    color: var(--orange); font-size: 27px; font-weight: 600; line-height: 26px;
  }
  .step--1 { left: 58px; top: 88px; }
  .step--2 { left: 378px; top: 88px; }
  .step--3 { left: 352px; top: 180px; }
  .step--4 { left: 209px; top: 246px; }
  .step--5 { left: 89px; top: 180px; }
  .phone-name {
    left: 222px; width: 92px; top: 143px; text-align: center;
    color: var(--teal-deep); font-size: 10px; font-weight: 700;
  }
  .info-lead {
    left: 0; width: 560px; top: 306px; text-align: center;
    font-size: 15px; font-weight: 500;
  }
  .info-lead__url { color: var(--orange); }
  .info-notes {
    left: 0; width: 560px; top: 328px; text-align: center;
    font-size: 8.6px; font-weight: 500; line-height: 13px;
  }
</style>
</head>
<body>

<section class="card card--front" aria-label="Flyer front">
  <svg class="card__art" viewBox="0 0 560 374">
    <defs>
      <linearGradient id="shopper-tones" x1="0" y1="0" x2="1" y2="1">
        <stop offset="0" stop-color="#efe7e2"/>
        <stop offset="0.45" stop-color="#8e2433"/>
        <stop offset="1" stop-color="#4f1620"/>
      </linearGradient>
    </defs>
    <rect width="560" height="374" fill="var(--teal)"/>
    <path d="M300 70 C330 20 400 20 430 30 C450 10 500 0 560 0 L560 345 C520 350 470 340 430 330 C380 320 330 290 300 240 C270 190 275 120 300 70 Z" fill="var(--orange)"/>
    <path d="M330 60 C370 15 450 20 500 60 C550 100 545 200 500 250 C460 300 380 300 340 250 C300 200 295 105 330 60 Z" fill="var(--pink)"/>
    <circle cx="365" cy="32" r="26" fill="var(--white)"/>
    <circle cx="535" cy="106" r="24" fill="none" stroke="var(--white)" stroke-width="4"/>
    <rect x="36" y="0" width="42" height="30" rx="4" fill="var(--white)" opacity="0.35" role="img" aria-label="Dot grid accent"/>
    <path d="M245 374 L240 205 C250 175 300 160 340 160 C360 130 420 120 450 150 C470 175 480 200 515 215 L520 374 Z" fill="url(#shopper-tones)" role="img" aria-label="Photo: woman in sunglasses and a burgundy coat holding shopping bags"/>
  </svg>
  <p class="card__text tagline-vertical">Stay Home</p>
  <h1 class="card__text headline">&amp; SHOP<br>ONLINE</h1>
  <span class="headline__divider"></span>
  <p class="card__text offer">Choose<br>from 1000+<br>KOREAN<br>products</p>
  <div class="brand-badge"><span class="brand-badge__name">MapleTrove</span></div>
</section>

<section class="card card--back" aria-label="Flyer back">
  <svg class="card__art" viewBox="0 0 560 374">
    <rect width="560" height="374" fill="var(--teal)"/>
    <path d="M0 90 C40 70 60 120 70 180 C80 240 120 280 160 300 C130 310 80 300 40 280 C10 260 0 230 0 200 Z" fill="var(--orange)"/>
    <path d="M90 0 L140 0 C120 10 100 20 90 0 Z" fill="var(--orange)"/>
    <path d="M480 40 C520 70 530 140 500 200 C480 240 460 260 440 280 C470 240 480 200 470 170 C460 120 470 80 480 40 Z" fill="var(--orange)"/>
    <path d="M250 285 C320 295 380 290 420 275 C380 300 300 300 250 285 Z" fill="var(--orange)"/>
    <path d="M60 90 C70 30 130 0 200 0 L460 0 C520 20 540 90 515 150 C495 200 470 230 460 260 C440 300 360 300 300 285 C230 270 180 300 120 270 C70 245 50 170 60 90 Z" fill="var(--pink)"/>
    <circle cx="22" cy="104" r="21" fill="var(--white)"/>
    <circle cx="490" cy="222" r="31" fill="none" stroke="#eeeeee" stroke-width="4"/>
    <rect x="476" y="0" width="46" height="44" rx="4" fill="var(--white)" opacity="0.35" role="img" aria-label="Dot grid accent"/>
    <rect x="0" y="300" width="38" height="66" rx="4" fill="var(--orange)" opacity="0.5" role="img" aria-label="Dot grid accent"/>

    <g class="phone">
      <rect x="222" y="76" width="92" height="144" rx="9" fill="var(--ink)"/>
      <rect x="229" y="86" width="78" height="112" fill="#f4f4f4"/>
      <rect x="231" y="90" width="74" height="4" fill="#cfd6d9"/>
      <rect x="231" y="96" width="74" height="22" fill="var(--screen-blue)"/>
      <rect x="231" y="120" width="74" height="10" fill="var(--orange)"/>
      <rect x="235" y="182" width="24" height="3" fill="#b8b8b8"/>
      <rect x="277" y="182" width="24" height="3" fill="#b8b8b8"/>
      <circle cx="268" cy="209" r="4" fill="#1c2226"/>
    </g>

    <g class="arrows" stroke="var(--white)" stroke-width="2.2" fill="var(--white)">
      <line x1="158" y1="102" x2="205" y2="113"/><path d="M214 115 L203 108 L201 118 Z"/>
      <line x1="320" y1="121" x2="358" y2="113"/><path d="M367 111 L356 107 L358 117 Z"/>
      <line x1="368" y1="174" x2="330" y2="153"/><path d="M322 148 L329 158 L334 150 Z"/>
      <line x1="216" y1="152" x2="180" y2="172"/><path d="M172 176 L184 175 L179 167 Z"/>
    </g>

    <g class="icons" fill="none" stroke="var(--orange)" stroke-width="1.5">
      <rect x="106" y="62" width="14" height="14" rx="1"/><path d="M101 79 L110 74 L116 77"/>
      <path d="M414 78 L426 66 L433 72 L421 84 Z"/><circle cx="429" cy="70" r="1.5"/>
      <rect x="388" y="158" width="16" height="16"/><path d="M392 158 V154 A4 4 0 0 1 400 154 V158"/>
      <rect x="132" y="156" width="16" height="12"/><path d="M148 160 H155 L158 165 V168 H148"/><circle cx="137" cy="170" r="2.5"/><circle cx="153" cy="170" r="2.5"/>
      <circle cx="274" cy="230" r="7"/><path d="M269 235 L262 242"/>
    </g>
  </svg>

  <h2 class="card__text back-title">How it works</h2>
  <p class="card__text phone-name">MapleTrove</p>
  <div class="card__text step step--1"><span class="step__num">1</span><span>PAYMENT &amp;<br>REQUEST</span></div>
  <div class="card__text step step--2"><span class="step__num">2</span><span>ORDER &amp;<br>PURCHASE</span></div>
  <div class="card__text step step--3"><span class="step__num">3</span><span>ITEM<br>DELIVERY</span></div>
  <div class="card__text step step--4"><span class="step__num">4</span><span>INSPECTION &amp;<br>APPROVAL</span></div>
  <div class="card__text step step--5"><span class="step__num">5</span><span>PACKING &amp;<br>SHIPPING</span></div>

  <p class="card__text info-lead">For more information, visit <span class="info-lead__url">www.mapletrove.com</span></p>
  <p class="card__text info-notes">Our customer service is in English. We accept credit cards &amp; PayLoop payments.<br>No need to sign up anywhere. Shop on any website in Korea, with us. We ship worldwide.</p>
</section>

</body>
</html>
```